Business card design

I need my logo on this card, things I need the card to have on it
licensed and insured.
owner operators Derek & Milton Halvorsen
my phone number 5418237906
Disaster Recovery, Storm Damage Restoration, Proactive Disaster Plan Management, Roof Repair/Restoration Structural Repair and Reconstruction, Emergency Boarding and Tarping Service, Perimeter Fencing, Emergency Tree Removal,

```html
<!DOCTYPE html>
<html lang="en">
<head>
<meta charset="utf-8">
<title>Halvorsen's Construction – Stationery</title>
<link href="https://fonts.googleapis.com/css2?family=Montserrat:wght@400;500&family=Lato:wght@400&display=swap" rel="stylesheet">
<style>
  :root{
    --blue:#3a8fd6;
    --grey:#6d6e71;
    --ink:#3a3a3a;
    --paper:#ffffff;
    --stage-light:#b9b9bb;
  }
  *{box-sizing:border-box;margin:0;padding:0}
  html,body{width:1200px;height:520px;overflow:hidden}
  body{background:linear-gradient(180deg,#9c9c9c 0%,#7a7a7a 55%,#666 100%);font-family:"Lato",sans-serif;color:var(--ink);position:relative}
  .stage-side{position:absolute;left:769px;top:0;width:431px;height:520px;background:var(--stage-light)}
  .sheet{position:absolute;background:var(--paper);box-shadow:4px 6px 12px rgba(0,0,0,.35)}

  /* Wordmark: one colour, one weight, plain square beside it */
  .brand{display:flex;align-items:center;gap:.35em;font-family:"Montserrat",sans-serif;font-weight:500;color:var(--grey);line-height:1;white-space:nowrap}
  .brand .mark{display:block;width:.7em;height:.7em;background:var(--blue);flex:none}

  .mont{font-family:"Montserrat",sans-serif}
  .icon{width:4px;height:4px;vertical-align:-0.5px;margin-right:1.5px}

  /* Letterhead */
  .letterhead{left:53px;top:52px;width:294px;height:415px}
  .letterhead .brand{position:absolute;left:27px;top:66px;font-size:10px}
  .lh-address{position:absolute;right:99px;top:30px;text-align:right;font-size:5.2px;line-height:7.4px;color:var(--grey)}
  .lh-address .org{color:var(--blue)}
  .lh-rule{position:absolute;left:202px;top:30px;width:.5px;height:21px;background:var(--grey)}
  .lh-contact{position:absolute;left:208px;top:31px;font-size:5px;line-height:6px;color:#222}
  .recipient{position:absolute;left:27px;top:110px;font-size:5.4px;line-height:7.3px}
  .recipient .who{font-size:5.8px}
  .recipient small{font-size:4.4px;display:block}
  .letter-body{position:absolute;left:27px;top:144px;width:240px;font-size:4.3px;line-height:7.2px;text-align:justify;color:#444}
  .letter-body p{margin-bottom:6px}
  .sign-off{position:absolute;left:27px;top:284px;font-size:5px}

  /* Business cards */
  .card{top:63px;width:134px;height:76px;border-radius:3px}
  .card-front{left:407px}
  .card-back{left:551px}
  .card-front .brand{position:absolute;left:5px;top:8px;font-size:8.5px}
  .card-owners{position:absolute;left:0;top:27px;padding-left:5px;border-left:2px solid var(--blue);font-size:5px;line-height:5px}
  .card-owners .names{color:var(--blue)}
  .card-owners .names em{font-style:normal;color:var(--grey)}
  .card-owners small{display:block;font-size:3.4px;line-height:4.4px;color:#222}
  .card-details{position:absolute;left:5px;top:45px;font-size:3.6px;line-height:4.9px;color:#222}
  .card-details .gap{height:3px}
  .card-back .brand{position:absolute;left:0;right:0;top:38px;justify-content:center;font-size:7px}
  .services{position:absolute;left:5px;right:5px;top:57px;font-size:3.1px;line-height:4.8px;color:#222;text-align:center}

  /* Envelope */
  .envelope-flap{left:400px;top:187px;width:285px;height:125px;overflow:hidden}
  .flap-curve{position:absolute;left:0;top:0;width:285px;height:38px;background:var(--paper);border-radius:0 0 30px 30px;box-shadow:0 2px 3px rgba(0,0,0,.22)}
  .flap-curve .brand{position:absolute;left:0;right:0;top:14px;justify-content:center;font-size:6px}
  .envelope-front{left:400px;top:345px;width:285px;height:122px}
  .envelope-front .brand{position:absolute;left:6px;top:17px;font-size:5.6px}
  .env-rule{position:absolute;left:96px;top:8px;width:.5px;height:23px;background:var(--grey)}
  .env-address{position:absolute;left:102px;top:15px;font-size:4.3px;line-height:5.6px;color:#222}

  /* Folder */
  .folder-cover{left:797px;top:28px;width:372px;height:220px}
  .folder-cover .brand{position:absolute;left:22px;top:92px;font-size:21px}
  .cover-contact{position:absolute;left:22px;bottom:16px;font-size:7px;line-height:8.5px;color:#222}
  .cover-address{position:absolute;right:22px;bottom:22px;font-size:7px;line-height:8.5px;color:#222;text-align:right}
  .folder-inside{left:797px;top:268px;width:372px;height:230px;background:#f3f3f3;overflow:hidden}
  .inside-divider{position:absolute;left:185px;top:0;width:1px;height:100%;background:#cfcfcf}
  .pocket-left{position:absolute;left:0;bottom:0;width:186px;height:70px;background:var(--blue);border-radius:0 40px 0 0}
  .pocket-right{position:absolute;right:0;bottom:0;width:186px;height:90px;background:var(--grey);border-radius:40px 0 0 0}
  .mini-letter{position:absolute;left:212px;top:12px;width:130px;height:184px;background:var(--paper);box-shadow:1px 2px 4px rgba(0,0,0,.2)}
  .mini-letter .brand{position:absolute;left:10px;top:24px;font-size:4.6px}
  .mini-lines{position:absolute;left:10px;right:10px;top:48px}
  .mini-lines span{display:block;height:1px;background:#c8c8c8;margin-bottom:2.4px}
</style>
</head>
<body>
<svg width="0" height="0" style="position:absolute" aria-hidden="true">
  <symbol id="ic-phone" viewBox="0 0 10 10"><path d="M2 1l2 2-1 1.2c.6 1.3 1.5 2.2 2.8 2.8L7 6l2 2-1.2 1.3C4.5 9 1 5.5.7 2.2z" fill="#3a8fd6"/></symbol>
  <symbol id="ic-mail" viewBox="0 0 10 10"><rect x="1" y="2.5" width="8" height="5.5" rx=".8" fill="#3a8fd6"/><path d="M1.3 3l3.7 2.8L8.7 3" stroke="#fff" stroke-width=".8" fill="none"/></symbol>
  <symbol id="ic-web" viewBox="0 0 10 10"><circle cx="5" cy="5" r="4" fill="#3a8fd6"/><path d="M1 5h8M5 1c-2 2.5-2 5.5 0 8M5 1c2 2.5 2 5.5 0 8" stroke="#fff" stroke-width=".6" fill="none"/></symbol>
</svg>

<div class="stage-side"></div>

<!-- Letterhead -->
<section class="sheet letterhead">
  <div class="brand"><span class="mark"></span><span class="name">Halvorsen's Construction</span></div>
  <div class="lh-address mont"><span class="org">Northfield Group</span><br>418 Alder Street, Suite 210<br>Fremont, CA 94536</div>
  <div class="lh-rule"></div>
  <div class="lh-contact mont">
    <div><svg class="icon"><use href="#ic-phone"/></svg>5418237906</div>
    <div><svg class="icon"><use href="#ic-mail"/></svg>info@halvorsenco.com</div>
    <div><svg class="icon"><use href="#ic-web"/></svg>www.yourwebsite.com</div>
  </div>
  <div class="recipient">
    <div class="who">MARISA OLDEN</div>
    <small>Chief Executive Officer</small>
    <small>City/State, Zip Code</small>
  </div>
  <div class="letter-body">
    <p>Proin gravida nibh vel velit auctor aliquet. Aenean sollicitudin, lorem quis bibendum auctor, nisi elit consequat ipsum, nec sagittis sem nibh id elit. Duis sed odio sit amet nibh vulputate cursus a sit amet mauris. Morbi accumsan ipsum velit. Nam nec tellus a odio tincidunt auctor a ornare odio. Sed non mauris vitae erat consequat auctor eu in elit. Class aptent taciti sociosqu ad litora torquent ugue. Sed non neque elit. Sed ut imperdiet nisi. Proin condimentum fermentum nunc. Etiam pharetra, imperdiet nisi. Proin condimentum fermentum nunc. Etiam pharetra, erat sed fermentum feugiat, velit mauris egestas quam, ut aliquam massa nisl quis neque. Suspendisse in orci enim.</p>
    <p>This is a sample version of Lorem Ipsum. Proin gravida nibh vel velit auctor aliquet. Aenean sollicitudin, lorem quis bibendum auctor, nisi elit consequat ipsum, nec sagittis sem nibh id elit. Duis sed odio sit amet nibh vulputate cursus a sit amet mauris. Mo rbi accumsan ipsum velit. Nam nec tellus a odio tincidunt auctor a ornare odio. Sed non mauris vitae erat consequat auctor eu in elit. Class aptt consequat auctor eu in elit. Class aptent taciti sociosqu ad litora torquent per conubia nostra, per inceptos himenaeos. Mauris in erat justo.</p>
    <p>Nullam ac urna eu felis dapibus condimentum sit amet a augue. Sed non neque elit. Sed ut imperdiet nisi. Proin condimentum fermentum nunc. Etiam pharetra, erat sed fermentum feugiat, velit mauris egestas quam.Nullam ac urna eu felis dapibus condimentum sit amet a aug pharetra, erat sed fermentum feugiat, velit mauris egestas quam.Nullam ac urna eu felis dapibus condimentum sit amet a augue. Sed non neque elit. Sed ut imperdiet nisi. Proin condimentum fermentum nunc.</p>
  </div>
  <div class="sign-off">Sincerely,</div>
</section>

<!-- Business card front -->
<section class="sheet card card-front">
  <div class="brand"><span class="mark"></span><span class="name">Halvorsen's Construction</span></div>
  <div class="card-owners mont">
    <span class="names">Derek &amp; Milton <em>Halvorsen</em></span>
    <small>owner operators</small>
    <small>licensed and insured</small>
  </div>
  <div class="card-details mont">
    <div>Your address, City</div>
    <div>State, Zip 1234</div>
    <div class="gap"></div>
    <div><svg class="icon"><use href="#ic-phone"/></svg>5418237906</div>
    <div><svg class="icon"><use href="#ic-mail"/></svg>info@halvorsenco.com</div>
    <div><svg class="icon"><use href="#ic-web"/></svg>www.yourwebsite.com</div>
  </div>
</section>

<!-- Business card back -->
<section class="sheet card card-back">
  <div class="brand"><span class="mark"></span><span class="name">Halvorsen's Construction</span></div>
  <p class="services mont">Disaster Recovery, Storm Damage Restoration, Proactive Disaster Plan Management, Roof Repair/Restoration Structural Repair and Reconstruction, Emergency Boarding and Tarping Service, Perimeter Fencing, Emergency Tree Removal.</p>
</section>

<!-- Envelope back -->
<section class="sheet envelope-flap">
  <div class="flap-curve">
    <div class="brand"><span class="mark"></span><span class="name">Halvorsen's Construction</span></div>
  </div>
</section>

<!-- Envelope front -->
<section class="sheet envelope-front">
  <div class="brand"><span class="mark"></span><span class="name">Halvorsen's Construction</span></div>
  <div class="env-rule"></div>
  <div class="env-address mont">Your address, City<br>State, Zip 1234</div>
</section>

<!-- Folder cover -->
<section class="sheet folder-cover">
  <div class="brand"><span class="mark"></span><span class="name">Halvorsen's Construction</span></div>
  <div class="cover-contact mont">
    <div><svg class="icon" style="width:6px;height:6px"><use href="#ic-phone"/></svg>5418237906</div>
    <div><svg class="icon" style="width:6px;height:6px"><use href="#ic-mail"/></svg>info@halvorsenco.com</div>
    <div><svg class="icon" style="width:6px;height:6px"><use href="#ic-web"/></svg>www.yourwebsite.com</div>
  </div>
  <div class="cover-address mont">Your address, City<br>State, Zip 1234</div>
</section>

<!-- Folder inside -->
<section class="sheet folder-inside">
  <div class="inside-divider"></div>
  <div class="pocket-left"></div>
  <div class="mini-letter">
    <div class="brand"><span class="mark"></span><span class="name">Halvorsen's Construction</span></div>
    <div class="mini-lines">
      <span style="width:30%"></span><span style="width:22%"></span><span style="width:0;margin-bottom:6px"></span>
      <span></span><span></span><span></span><span></span><span style="width:60%;margin-bottom:6px"></span>
      <span></span><span></span><span></span><span></span><span style="width:55%;margin-bottom:6px"></span>
      <span></span><span></span><span></span><span style="width:40%"></span>
    </div>
  </div>
  <div class="pocket-right"></div>
</section>
</body>
</html>
```